Flyer needed For the Council for Stewardship of Public Works

With an increasing need for professional staffing in our design and construction industry it is important for organizations to be able to attract, support, and retain people of all genders. With the increase of women entering the design/construction industry, we need to be able to identify and address the specific needs of women in our industry, including those A/E’s who are on the facility Owner side.

This Forum will provide a venue to openly discuss the issues affecting our industry and ideas to address those issues.The program includes time for presentations and a panel discussion by accomplished women in our industry, and facilitated table and open discussions to form solutions with your peers. You will come away with ideas you can implement within your organization to build processes and a supportive culture for women

IN THE ATTACHMENTS
* you'll find our company logo

Target Market(s)

Women in the design and construction industry

Industry/Entity Type

Construction

Requirements
Must have
• Logo, event name, date, time, location, panelists names and pics, NBF continuing education provided, contact information: Maren Holtzclaw, maren.holtzclaw@c-sfpw.org, (555) 740-1938
• Register at: www.c-sfpw.org/events
• Design should encompass the description given above.
Nice to have
• Colors that compliment our logo

```html
<!DOCTYPE html>
<html lang="en">
<head>
<meta charset="utf-8">
<title>Women's Mini-Forum &amp; Workshop Flyer</title>
<link rel="stylesheet" href="https://fonts.googleapis.com/css2?family=Russo+One&family=Oswald:wght@500;600&family=Open+Sans:wght@400;600&display=swap">
<style>
  :root {
    --ink-black: #000000;
    --stone-grey: #c9c9c9;
    --date-grey: #bdbdbd;
    --leaf-green: #8dc63f;
    --sky-blue: #3f7fc4;
    --deep-blue: #1f4f95;
    --paper-white: #ffffff;
    --muted-grey: #9a9a9a;
  }
  * { margin: 0; padding: 0; box-sizing: border-box; }
  html, body {
    width: 849px;
    height: 1200px;
    overflow: hidden;
    background: var(--ink-black);
  }
  .flyer {
    position: relative;
    width: 849px;
    height: 1200px;
    background: var(--ink-black);
    color: var(--paper-white);
    text-align: center;
    font-family: "Open Sans", sans-serif;
  }
  .brand-mark {
    position: absolute;
    left: 329px;
    top: 34px;
    width: 190px;
    height: 190px;
  }
  .brand-mark svg { display: block; }
  .brand-name {
    position: absolute;
    left: 0;
    right: 0;
    top: 232px;
    font-family: "Russo One", sans-serif;
    font-size: 26px;
    color: var(--paper-white);
    letter-spacing: 1px;
  }
  .event-title {
    position: absolute;
    left: 0;
    right: 0;
    top: 296px;
    font-family: "Russo One", sans-serif;
    font-weight: 400;
    line-height: 1;
  }
  .event-title .line-audience {
    display: block;
    font-size: 60px;
    color: var(--stone-grey);
  }
  .event-title .line-format {
    display: block;
    margin-top: 16px;
    font-size: 60px;
    color: var(--leaf-green);
  }
  .event-title .amp { color: var(--sky-blue); }
  .event-date {
    position: absolute;
    left: 0;
    right: 0;
    top: 458px;
    font-family: "Oswald", sans-serif;
    font-weight: 600;
    font-size: 52px;
    line-height: 1.2;
    color: var(--date-grey);
    letter-spacing: 1px;
  }
  .event-date .year { color: var(--paper-white); }
  .event-venue {
    position: absolute;
    left: 0;
    right: 0;
    top: 536px;
    font-size: 28px;
    color: var(--paper-white);
  }
  .event-time {
    position: absolute;
    left: 0;
    right: 0;
    top: 580px;
    font-size: 22px;
    color: var(--date-grey);
  }
  .panel-heading {
    position: absolute;
    left: 0;
    right: 0;
    top: 636px;
    font-family: "Oswald", sans-serif;
    font-weight: 500;
    font-size: 26px;
    letter-spacing: 2px;
    color: var(--leaf-green);
    text-transform: uppercase;
  }
  .panelists {
    position: absolute;
    left: 112px;
    top: 690px;
    width: 625px;
    display: flex;
    justify-content: space-between;
    list-style: none;
  }
  .panelist { width: 190px; }
  .panelist-photo {
    width: 130px;
    height: 130px;
    margin: 0 auto;
    border-radius: 50%;
    border: 4px solid var(--sky-blue);
    background: linear-gradient(160deg, #5b5b5b, #2a2a2a);
  }
  .panelist-name {
    margin-top: 12px;
    font-size: 18px;
    font-weight: 600;
    color: var(--paper-white);
  }
  .panelist-role {
    margin-top: 2px;
    font-size: 14px;
    color: var(--muted-grey);
  }
  .info-block {
    position: absolute;
    left: 60px;
    top: 934px;
    width: 570px;
    text-align: left;
  }
  .register {
    font-family: "Oswald", sans-serif;
    font-weight: 500;
    font-size: 26px;
    color: var(--stone-grey);
  }
  .register .url { color: var(--leaf-green); }
  .contact {
    margin-top: 14px;
    font-size: 19px;
    line-height: 1.5;
    color: var(--paper-white);
  }
  .contact .label { color: var(--sky-blue); font-weight: 600; }
  .credit-note {
    margin-top: 16px;
    font-size: 17px;
    color: var(--date-grey);
  }
  .credit-badge {
    position: absolute;
    left: 664px;
    top: 1004px;
    width: 170px;
    height: 170px;
  }
</style>
</head>
<body>
  <main class="flyer">
    <div class="brand-mark">
      <svg width="190" height="190" viewBox="0 0 190 190" aria-hidden="true">
        <circle cx="95" cy="95" r="92" fill="var(--sky-blue)" stroke="var(--deep-blue)" stroke-width="5"/>
      </svg>
      <span class="brand-name">C-SfPW</span>
    </div>

    <h1 class="event-title">
      <span class="line-audience">AEC Industry Women's</span>
      <span class="line-format">Mini-Forum <span class="amp">&amp;</span> Workshop</span>
    </h1>

    <p class="event-date">JANUARY 13 <span class="year">2016</span></p>
    <p class="event-venue">Harborline Suites, San Marcos, Texas</p>
    <p class="event-time">8:30 AM – 4:00 PM</p>

    <h2 class="panel-heading">Featured Panelists</h2>
    <ul class="panelists">
      <li class="panelist">
        <div class="panelist-photo" role="img" aria-label="Portrait photo of panelist Renata Vollmer"></div>
        <p class="panelist-name">Renata Vollmer</p>
        <p class="panelist-role">Principal Architect</p>
      </li>
      <li class="panelist">
        <div class="panelist-photo" role="img" aria-label="Portrait photo of panelist Dana Okafor-Lind"></div>
        <p class="panelist-name">Dana Okafor-Lind</p>
        <p class="panelist-role">Construction Manager</p>
      </li>
      <li class="panelist">
        <div class="panelist-photo" role="img" aria-label="Portrait photo of panelist Priya Castellane"></div>
        <p class="panelist-name">Priya Castellane</p>
        <p class="panelist-role">Facilities Director</p>
      </li>
    </ul>

    <section class="info-block">
      <p class="register">Register at: <span class="url">www.c-sfpw.org/events</span></p>
      <p class="contact">
        <span class="label">Contact:</span> Maren Holtzclaw<br>
        maren.holtzclaw@c-sfpw.org<br>
        (555) 740-1938
      </p>
      <p class="credit-note">NBF continuing education credits provided</p>
    </section>

    <svg class="credit-badge" viewBox="0 0 170 170" aria-hidden="true">
      <circle cx="85" cy="85" r="81" fill="var(--paper-white)"/>
    </svg>
  </main>
</body>
</html>
```